Tumble Tail (Pet Supplies) Home Page

For our Tumble Tail website, we want this to be fun and playful but with a touch of your creativity! Tumble Tail is a fun-loving brand that sells pet supplies and accessories focused on accentuating the love between pets and their owners. We want to advertise these products in a welcoming way, making the customer receive the happiness the brand offers.

Target Market(s)

Main demo: Female pet owners online shopping 18-34. Secondary demo: All pet owners online shopping 18-34.

Number of Pages Required

1 page

```html
<!DOCTYPE html>
<html lang="en">
<head>
<meta charset="utf-8">
<title>Tumble Tail – Pet Supplies</title>
<link rel="stylesheet" href="https://fonts.googleapis.com/css2?family=Roboto:ital,wght@0,400;0,500;0,700;1,400&family=Sniglet:wght@400;800&display=swap">
<style>
:root{
  --ink:#111;
  --black:#000;
  --white:#fff;
  --purple:#8d3fa6;
  --teal:#27c3cb;
  --orange:#ff8a3d;
  --star:#f5b800;
  --footer:#1c1b1b;
}
*{box-sizing:border-box;margin:0;padding:0}
html,body{width:1200px;height:3243px;overflow:hidden;background:var(--white)}
body{position:relative;font-family:"Roboto",sans-serif;color:var(--ink)}
.abs{position:absolute}
.display{font-family:"Sniglet",cursive;font-weight:800}

.promo-bar{left:0;top:0;width:1200px;height:44px;background:var(--black);color:var(--white);font-size:14px;display:flex;align-items:center;justify-content:center}

.site-header{left:0;top:44px;width:1200px;height:79px;background:var(--white);box-shadow:0 2px 4px rgba(0,0,0,.06)}
.brand{left:100px;top:27px;display:flex;align-items:center;gap:8px;font-family:"Sniglet",cursive;font-weight:800;font-size:19px;color:var(--teal)}
.brand-dot{width:20px;height:20px;border-radius:50%;background:var(--teal)}
.main-nav{left:292px;top:31px;display:flex;font-size:15px;font-weight:500}
.main-nav span{padding:0 14px}
.main-nav .active{color:var(--purple);padding-left:0}
.search{left:825px;top:19px;width:182px;height:38px;border:1px solid #ccc;border-radius:19px;font-size:12px;color:#555;padding:11px 20px}
.search svg{position:absolute;right:14px;top:10px}
.cart{left:1031px;top:23px;display:flex;gap:6px;align-items:center}
.cart-text{font-size:12px;line-height:13px;font-weight:500}
.cart-text small{font-size:11px;font-weight:400}

.hero{left:0;top:123px;width:1200px;height:538px;background:linear-gradient(180deg,#b9d4ea 0%,#d4e2ec 40%,#6a8ca6 62%,#d8c3a3 80%,#cdb28b 100%)}
.hero-photo{left:520px;top:123px;width:680px;height:538px;background:radial-gradient(ellipse at 40% 40%,#c98c3e 0%,#b87a35 35%,rgba(240,235,230,.8) 60%,rgba(220,210,200,0) 80%)}
.hero-title{left:130px;top:268px;font-size:56px;color:var(--black);line-height:1}
.hero-copy{left:132px;top:350px;width:380px;font-size:15.5px;line-height:25px}
.btn-shop{left:135px;top:424px;width:156px;height:43px;border-radius:22px;background:var(--orange);color:var(--white);font-weight:700;font-size:14px;display:flex;align-items:center;justify-content:center;gap:8px}
.dots{left:570px;top:621px;display:flex;gap:10px}
.dots i{width:12px;height:12px;border-radius:50%;border:1.5px solid var(--white)}
.dots i.on{background:var(--white)}

.sale-text{left:0;top:680px;width:1200px;text-align:center;color:var(--white);font-size:30px;font-family:"Sniglet",cursive;font-weight:400;letter-spacing:.5px}

.section-mark{width:40px;height:40px;border-radius:50%;border:5px solid var(--teal)}
.section-title{width:1200px;left:0;text-align:center;font-size:40px;line-height:1;color:var(--black)}

.tile-overlay{display:flex;align-items:center;justify-content:center;background:rgba(150,70,185,.78)}

.paylater{left:0;top:2113px;width:1200px;height:214px;background:var(--teal)}
.paylater-title{left:201px;top:2164px;font-size:40px;line-height:58px;color:var(--white)}
.partner{color:var(--white);font-weight:500;font-size:48px;display:flex;align-items:center;gap:14px}
.partner i{width:40px;height:40px;border-radius:50%;background:var(--white)}

.card{width:315px;height:188px;background:var(--white);box-shadow:0 4px 14px rgba(0,0,0,.08)}
.avatar{width:88px;height:88px;border-radius:50%;border:4px solid var(--teal)}
.who{font-size:12px;font-weight:500}
.stars{color:var(--star);font-size:16px;letter-spacing:1px}
.quote{font-size:13.5px;line-height:22px;font-style:italic}
.qmark{font-family:"Sniglet",cursive;font-weight:800;color:var(--teal);font-size:62px;line-height:1}

.footer{left:0;top:2830px;width:1200px;height:413px}
.f-brand{left:110px;top:3040px;font-family:"Sniglet",cursive;font-weight:800;font-size:24px;color:var(--white);display:flex;align-items:center;gap:8px}
.f-brand i{width:24px;height:24px;border-radius:50%;background:var(--white)}
.social{width:32px;height:32px;border-radius:50%;background:var(--teal)}
.btn-rewards{left:110px;top:3135px;width:138px;height:40px;border-radius:20px;background:var(--orange);color:var(--white);font-size:14px;font-weight:500;display:flex;align-items:center;justify-content:center}
.f-head{color:var(--white);font-size:16px;font-weight:700}
.f-link{color:var(--white);font-size:14px}
.f-text{left:797px;top:2975px;width:300px;color:var(--white);font-size:13.5px;line-height:24px}
.newsletter{left:796px;top:3034px;width:292px;height:41px;border:1px solid var(--white);border-radius:21px;overflow:hidden;display:flex}
.newsletter span{flex:1;color:var(--white);font-size:12px;padding:13px 12px}
.newsletter b{width:111px;background:var(--orange);color:var(--white);font-size:15px;font-weight:500;display:flex;align-items:center;justify-content:center}
.phone{left:806px;top:3100px;color:var(--white);font-size:17px;display:flex;align-items:center;gap:10px}
.chat{left:1029px;top:3088px;width:52px;height:52px;border-radius:12px;background:var(--teal);display:flex;align-items:center;justify-content:center}
.rule{left:110px;top:3185px;width:978px;height:1px;background:#555}
.copyright{left:0;top:3205px;width:1200px;text-align:center;color:var(--white);font-size:14px}
</style>
</head>
<body>

<div class="abs promo-bar">“Free shipping on all orders $50 and over!”</div>

<header class="abs site-header">
  <div class="abs brand"><i class="brand-dot"></i>Tumble Tail</div>
  <nav class="abs main-nav">
    <span class="active">SHOP</span><span>|</span><span>OUR STORY</span><span>|</span><span>BOOP BLOG</span><span>|</span><span>PET HISTORY 101</span>
  </nav>
  <div class="abs search">Search
    <svg width="16" height="16" viewBox="0 0 16 16"><circle cx="7" cy="7" r="5" fill="none" stroke="#333" stroke-width="1.5"/><line x1="11" y1="11" x2="15" y2="15" stroke="#333" stroke-width="1.5"/></svg>
  </div>
  <div class="abs cart">
    <svg width="28" height="24" viewBox="0 0 28 24"><path d="M2 8h24l-3 14H5z" fill="#27c3cb"/><path d="M8 8l6-6 6 6" fill="none" stroke="#27c3cb" stroke-width="2"/></svg>
    <div class="cart-text">CART<br><small>$.0.00</small></div>
  </div>
</header>

<section>
  <div class="abs hero" role="img" aria-label="Beach backdrop with sea and sky"></div>
  <div class="abs hero-photo" role="img" aria-label="Woman hugging a golden retriever on the beach"></div>
  <h1 class="abs hero-title display">Tumble Tail</h1>
  <p class="abs hero-copy">Lorem ipsum dolor sit amet, consectetur adipiscing elit, sed do eiusmod tempor incididunt</p>
  <div class="abs btn-shop">SHOP NOW
    <svg width="14" height="14" viewBox="0 0 14 14"><circle cx="7" cy="7" r="7" fill="#fff"/><path d="M5 4l3 3-3 3" fill="none" stroke="#ff8a3d" stroke-width="2"/></svg>
  </div>
  <svg class="abs" style="left:50px;top:375px" width="28" height="54" viewBox="0 0 28 54"><path d="M26 2L2 27l24 25" fill="none" stroke="#111" stroke-width="2"/></svg>
  <svg class="abs" style="left:1116px;top:375px" width="28" height="54" viewBox="0 0 28 54"><path d="M2 2l24 25L2 52" fill="none" stroke="#111" stroke-width="2"/></svg>
  <div class="abs dots"><i></i><i class="on"></i><i></i></div>
</section>

<svg class="abs" style="left:0;top:661px" width="1200" height="110" viewBox="0 0 1200 110">
  <path d="M0 0H1200V28Q600 150 0 28Z" fill="#27c3cb"/>
  <path d="M0 0H1200V20Q600 135 0 20Z" fill="#8d3fa6"/>
</svg>
<div class="abs sale-text">50% off sale going on now! Because we love you too”</div>

<section>
  <div class="abs section-mark" style="left:580px;top:838px"></div>
  <h2 class="abs section-title display" style="top:903px">Furry Favorites</h2>

  <div class="abs" style="left:100px;top:982px;width:324px;height:338px;background:linear-gradient(160deg,#c49063,#8a5a2f 60%,#b6b1aa)" role="img" aria-label="Beagle eating kibble from a steel bowl"></div>
  <div class="abs" style="left:438px;top:982px;width:324px;height:338px;background:radial-gradient(circle at 50% 50%,#9b5a34,#c23a3a 35%,#ece8e4 70%)" role="img" aria-label="Bowls of assorted pet food and treats"></div>
  <div class="abs" style="left:776px;top:982px;width:323px;height:688px;background:linear-gradient(180deg,#6c9a2a,#3d6b1c 50%,#7aa534)" role="img" aria-label="Goldfish and tropical fish eating flakes"></div>
  <div class="abs tile-overlay" style="left:100px;top:1332px;width:324px;height:338px" role="img" aria-label="Bowl of colourful kibble">
    <svg width="56" height="56" viewBox="0 0 56 56"><path d="M28 2v52M2 28h52" stroke="#fff" stroke-width="3"/></svg>
  </div>
  <div class="abs" style="left:438px;top:1332px;width:324px;height:338px;background:linear-gradient(180deg,#f2f1ee,#e3ddd5 60%,#b89468)" role="img" aria-label="Cat and shepherd dog sitting by their bowls"></div>
  <div class="abs" style="left:100px;top:1682px;width:324px;height:339px;background:linear-gradient(135deg,#6b665f,#3d3b39 50%,#e0592a 80%)" role="img" aria-label="Tabby cat eating from an orange bowl"></div>
  <div class="abs" style="left:438px;top:1682px;width:324px;height:339px;background:linear-gradient(180deg,#d4d2cc,#7a4b2a 60%,#a0744a)" role="img" aria-label="Bowl of kibble beside fresh vegetables"></div>
  <div class="abs" style="left:776px;top:1682px;width:323px;height:339px;background:linear-gradient(180deg,#cfc8bf,#c69a5c 55%,#8a6a45)" role="img" aria-label="Labrador lying beside a green food bowl"></div>
</section>

<section>
  <div class="abs paylater"></div>
  <div class="abs paylater-title display">BUY NOW,<br>PAY LATER</div>
  <div class="abs partner" style="left:503px;top:2192px"><i></i>Loafly</div>
  <div class="abs partner" style="left:773px;top:2192px">Paylio</div>
</section>

<section>
  <div class="abs" style="left:1032px;top:2442px;width:168px;height:480px;background:linear-gradient(180deg,#c27a3e,#a8652e 60%,#d9a06a)" role="img" aria-label="Brown dog peeking in"></div>
  <div class="abs" style="left:0;top:2505px;width:100px;height:416px;background:linear-gradient(180deg,#8b7a66,#cbbfae 60%,#efe9e2)" role="img" aria-label="Tabby cat peeking in"></div>

  <div class="abs section-mark" style="left:568px;top:2397px"></div>
  <h2 class="abs section-title display" style="top:2462px;width:1196px">Testimonials</h2>

  <div class="abs card" style="left:100px;top:2565px"></div>
  <div class="abs avatar" style="left:113px;top:2541px;background:linear-gradient(135deg,#8fb96b,#5e5e66)" role="img" aria-label="Portrait of Bella the dog"></div>
  <div class="abs who" style="left:218px;top:2582px">- BELLA (DOG)</div>
  <div class="abs stars" style="left:218px;top:2600px">★★★★★</div>
  <p class="abs quote" style="left:117px;top:2642px;width:285px">“Before Tumble Tail my human bought me gifts that made me want to dig a hole under the fence and run. Now I still dig, but it’s to bury all my awesome toys!”</p>
  <div class="abs qmark" style="left:376px;top:2732px">“</div>

  <div class="abs card" style="left:441px;top:2565px"></div>
  <div class="abs avatar" style="left:454px;top:2541px;background:linear-gradient(135deg,#9a9a98,#5b564f)" role="img" aria-label="Portrait of Leo the cat"></div>
  <div class="abs who" style="left:559px;top:2582px">- LEO (CAT)</div>
  <div class="abs stars" style="left:559px;top:2600px">★★★★★</div>
  <p class="abs quote" style="left:457px;top:2642px;width:285px">“My favorite thing to do is watch the birds out the window. Those birds are lucky my house is full of comfy stuff from Tumble Tail so I don’t ever want to leave.”</p>
  <div class="abs qmark" style="left:716px;top:2732px">“</div>

  <div class="abs card" style="left:781px;top:2565px"></div>
  <div class="abs avatar" style="left:794px;top:2541px;background:linear-gradient(135deg,#3e6fb8,#e8742d 60%,#b03a5a)" role="img" aria-label="Portrait of Dora the fish"></div>
  <div class="abs who" style="left:899px;top:2582px">- DORA (FISH)</div>
  <div class="abs stars" style="left:899px;top:2600px">★★★★★</div>
  <p class="abs quote" style="left:797px;top:2642px;width:290px">“I could rave about Tumble Tail until I was blue in the gills! Those other brands just seem a bit fishy to me.”</p>
  <div class="abs qmark" style="left:1056px;top:2732px">“</div>
</section>

<footer>
  <svg class="abs footer" viewBox="0 0 1200 413" width="1200" height="413" preserveAspectRatio="none">
    <path d="M0 95Q600 -40 1200 95V413H0Z" fill="#8d3fa6"/>
    <path d="M0 101Q600 -28 1200 101V413H0Z" fill="#1c1b1b"/>
  </svg>
  <div class="abs f-brand"><i></i>Tumble Tail</div>
  <div class="abs social" style="left:109px;top:3084px"></div>
  <div class="abs social" style="left:146px;top:3084px"></div>
  <div class="abs social" style="left:183px;top:3084px"></div>
  <div class="abs social" style="left:221px;top:3084px"></div>
  <div class="abs btn-rewards">Rewards</div>

  <div class="abs f-head" style="left:395px;top:2942px">COMPANY</div>
  <div class="abs f-link" style="left:395px;top:2980px">Shop</div>
  <div class="abs f-link" style="left:395px;top:3010px">Our Story</div>
  <div class="abs f-link" style="left:395px;top:3040px">Boop Blog</div>
  <div class="abs f-link" style="left:395px;top:3070px">Pet History 1010</div>

  <div class="abs f-head" style="left:597px;top:2942px">HELP</div>
  <div class="abs f-link" style="left:597px;top:2980px">Returns &amp; Exchanges</div>
  <div class="abs f-link" style="left:597px;top:3010px">FAQ</div>
  <div class="abs f-link" style="left:597px;top:3040px">help@tumbletail.com</div>
  <div class="abs f-link" style="left:597px;top:3070px">Search</div>

  <div class="abs f-head" style="left:797px;top:2942px">SIGN UP FOR OUR NEWSLETTER</div>
  <p class="abs f-text">Lorem ipsum dolor sit amet, consectetur acing elit, sed do eiusmod te incididunt</p>
  <div class="abs newsletter"><span>Enter Your Email</span><b>SUBMIT</b></div>
  <div class="abs phone">
    <svg width="14" height="14" viewBox="0 0 24 24"><path d="M6.6 10.8a15 15 0 006.6 6.6l2.2-2.2a1 1 0 011-.25 11.4 11.4 0 003.6.57 1 1 0 011 1V20a1 1 0 01-1 1A17 17 0 013 4a1 1 0 011-1h3.5a1 1 0 011 1 11.4 11.4 0 00.57 3.6 1 1 0 01-.25 1z" fill="#fff"/></svg>
    555 010 2040
  </div>
  <div class="abs chat">
    <svg width="28" height="26" viewBox="0 0 28 26"><path d="M14 2C7 2 2 6.5 2 12c0 3 1.5 5.6 4 7.4L5 24l5-3c1.3.3 2.6.5 4 .5 7 0 12-4.5 12-10S21 2 14 2z" fill="#fff"/><path d="M9 10h10M9 14h7" stroke="#27c3cb" stroke-width="2"/></svg>
  </div>
  <div class="abs rule"></div>
  <div class="abs copyright">Copyright 2021 tumbletail.com All rights reserved</div>
</footer>

</body>
</html>
```